Vo Lunec - Business Cards & Stationnery
Think Ahead, Vo Lunec
Professional
Odile Fenwar Quintanel
48 rue des Glycines Doréales
75020 Paris
France
odile@volunec.com
www.volunec.com
The business cards have to be at the european standard ie 8,5 x 5,4 cm (seems to be 3.35'' x 2.13'')
Same for the stationnery ie A4 format, 21 x 29,7 cm (seems to be 8,27'' x 11.7'')
Please use the logo, name of the company and the base line: Think Ahead, Vo Lunec

```html
<!DOCTYPE html>
<html lang="fr">
<head>
<meta charset="utf-8">
<title>Vo Lunec – Carte de visite</title>
<link rel="stylesheet" href="https://fonts.googleapis.com/css2?family=Open+Sans:wght@400;600;700&display=swap">
<style>
  :root {
    --page-bg: #ece9e4;
    --card-bg: #ffffff;
    --brand-purple: #5b2a86;
    --brand-purple-dark: #3f1a63;
    --ink: #3a3a3a;
    --ink-soft: #6a6a6a;
    --rule: #c9c9c9;
    --accent-line: #1c1c1c;
  }
  * { margin: 0; padding: 0; box-sizing: border-box; }
  html, body {
    width: 1200px; height: 780px; overflow: hidden;
    background: var(--page-bg);
    font-family: "Open Sans", Arial, sans-serif;
  }
  .business-card {
    position: absolute; left: 100px; top: 72px;
    width: 1000px; height: 635px;
    background: var(--card-bg);
    border-radius: 34px;
    overflow: hidden;
    box-shadow: 0 10px 30px rgba(0,0,0,0.18);
  }
  .header-band { position: absolute; left: 0; top: 0; width: 1000px; height: 220px; }
  .holder-name {
    position: absolute; right: 44px; top: 26px;
    color: #fff; font-weight: 600; font-size: 29px; letter-spacing: 0.2px;
  }
  .brand-block {
    position: absolute; left: 70px; top: 300px; width: 360px;
  }
  .brand-mark-row { display: flex; align-items: center; gap: 18px; }
  .brand-square { width: 42px; height: 42px; background: var(--brand-purple); flex: none; }
  .brand-name {
    font-size: 56px; font-weight: 400; color: var(--ink);
    letter-spacing: 2px; text-transform: uppercase; line-height: 1;
  }
  .brand-tagline {
    margin-top: 10px; font-size: 20px; color: var(--ink-soft);
    letter-spacing: 2.2px; text-transform: uppercase;
  }
  .divider {
    position: absolute; left: 468px; top: 240px;
    width: 2px; height: 250px; background: var(--rule);
  }
  .contact-block {
    position: absolute; left: 500px; top: 250px;
    color: var(--ink); font-size: 21px; line-height: 31px;
  }
  .address { margin-bottom: 30px; }
  .contact-line { display: flex; align-items: center; gap: 14px; }
  .contact-line svg { width: 20px; height: 20px; flex: none; }
</style>
</head>
<body>
  <article class="business-card">
    <svg class="header-band" viewBox="0 0 1000 220" aria-hidden="true">
      <defs>
        <linearGradient id="band-gradient" x1="0" y1="0" x2="1" y2="0">
          <stop offset="0" stop-color="var(--brand-purple-dark)"/>
          <stop offset="1" stop-color="var(--brand-purple)"/>
        </linearGradient>
      </defs>
      <path d="M0 0 H1000 V110 C820 95 640 100 470 150 C330 190 170 185 0 150 Z" fill="url(#band-gradient)"/>
      <path d="M0 150 C170 185 330 190 470 150 C640 100 820 95 1000 110 L1000 118 C820 104 640 112 470 160 C330 200 170 196 0 162 Z" fill="var(--accent-line)"/>
    </svg>
    <div class="holder-name">Odile Fenwar Quintanel</div>

    <div class="brand-block">
      <div class="brand-mark-row">
        <span class="brand-square"></span>
        <span class="brand-name">Vo Lunec</span>
      </div>
      <div class="brand-tagline">Think Ahead, Vo Lunec</div>
    </div>

    <div class="divider"></div>

    <div class="contact-block">
      <p class="address">48 rue des Glycines Doréales<br>75020 Paris, France</p>
      <p class="contact-line">
        <svg viewBox="0 0 20 20" aria-hidden="true"><rect x="5" y="1" width="10" height="18" rx="2" fill="var(--brand-purple)"/><rect x="7" y="4" width="6" height="9" fill="#fff"/></svg>
        +33 (0)6 47 18 52 90
      </p>
      <p class="contact-line">
        <svg viewBox="0 0 20 20" aria-hidden="true"><rect x="1" y="4" width="18" height="12" fill="var(--brand-purple)"/><path d="M1 4 L10 11 L19 4" fill="none" stroke="#fff" stroke-width="1.6"/></svg>
        odile@volunec.com
      </p>
      <p class="contact-line">
        <svg viewBox="0 0 20 20" aria-hidden="true"><circle cx="10" cy="10" r="8.5" fill="var(--brand-purple)"/><ellipse cx="10" cy="10" rx="3.5" ry="8.5" fill="none" stroke="#fff" stroke-width="1.2"/><line x1="1.5" y1="10" x2="18.5" y2="10" stroke="#fff" stroke-width="1.2"/></svg>
        www.volunec.com
      </p>
    </div>
  </article>
</body>
</html>
```